Accommodation in an Executive Apartment for rent could be a Bed and breakfast,

Currently have a website and like the overall look but it needs revamping and want to add an instant booking button, which I would do later as the unit has a channel manager. Also want to be able to post blogs, etc. Need it to be viewed well on smart phones/tablets. all information related to this unit is on the current site which is www.lorvenstaysmirrabrook.com.au if you would view websites similar to staywell.example and roamtrip.example Must be able to be coded in Wordpress

The current design is done in Wordpress so would want this functionality in any new design.

Target Market(s)

Workers at Quorran precinct, Canberra. Workers at Halvern centre Deakin, Workers at Marlow Peter Tenby Hospital, Workers at Brindlewood Hospital, Public Servants Woden, Workers in Deakin ACT

Industry/Entity Type

Accommodation

Number of Pages Required

5+ page

Font styles to use
Sans Serif

Colors
ec1f27

Requirements
Must have
• Must have a classy look about it. Less clicks through the better. Not to wordy. Hard hitting points,
Nice to have
• Would like to retain the same colour theme and look
Should not have
• anything tacky

```html
<!DOCTYPE html>
<html lang="en">
<head>
<meta charset="utf-8">
<title>Lorven executive bed &amp; breakfast</title>
<link href="https://fonts.googleapis.com/css2?family=Open+Sans:wght@400;600;700&family=Raleway:wght@500;600;700&display=swap" rel="stylesheet">
<style>
:root{
  --maroon:#5a0712;
  --maroon-deep:#4a0510;
  --ink:#3a2a2a;
  --muted:#6b6b6b;
  --white:#ffffff;
  --panel:rgba(30,28,28,.72);
  --field:rgba(120,115,110,.55);
  --footer-bg:#c9d0d6;
  --charcoal:#3a3a3a;
}
*{box-sizing:border-box;margin:0;padding:0}
html,body{width:680px;height:1200px;overflow:hidden}
body{position:relative;font-family:'Open Sans',sans-serif;color:var(--ink);background:var(--white)}
.abs{position:absolute}
/* header */
.topbar{left:0;top:0;width:680px;height:48px;background:var(--maroon)}
.brand{left:0;width:680px;top:13px;text-align:center;font-family:'Raleway',sans-serif;font-weight:600;font-size:17px;color:var(--white)}
.call{right:28px;top:16px;display:flex;align-items:center;gap:6px;color:var(--white)}
.call .ring{width:25px;height:25px;border:1px solid #fff;border-radius:50%;display:flex;align-items:center;justify-content:center}
.call small{display:block;font-size:6px;line-height:7px}
.call b{display:block;font-size:9px;font-weight:400;line-height:10px}
.nav{left:0;top:48px;width:680px;height:72px;background:var(--white)}
.nav ul{list-style:none;display:flex;position:absolute;left:104px;top:0;height:72px}
.nav li{font-size:6.5px;color:var(--maroon);padding:0 12.5px;line-height:72px;letter-spacing:.2px}
.nav li.active{background:var(--maroon);color:var(--white);padding:0 14px;line-height:77px}
/* hero */
.hero{left:0;top:120px;width:680px;height:374px;background:linear-gradient(100deg,#6d5a45 0%,#a8906c 35%,#d8c7a4 60%,#b89e78 100%)}
.search{left:0;top:172px;width:435px;height:260px;background:var(--panel);color:#eee}
.tab{top:28px;width:70px;height:44px;background:rgba(90,88,86,.8);text-align:center;font-size:8.5px}
.tab svg{display:block;margin:9px auto 5px}
.lbl{font-size:8.5px;color:#f0f0f0}
.field{height:19px;background:var(--field);font-size:7.5px;color:#ddd;display:flex;align-items:center;padding-left:9px;gap:8px}
.field.dim{color:#9a9a9a}
.btn-search{left:28px;top:211px;width:112px;height:27px;background:var(--maroon);color:#fff;font-size:12px;text-align:center;line-height:27px;letter-spacing:.5px}
/* features */
.feat{width:200px;text-align:center}
.circle{width:70px;height:70px;border-radius:50%;margin:0 auto;display:flex;align-items:center;justify-content:center;background:var(--maroon);border:2px solid #fff}
.circle.light{background:#fff;border:2px solid var(--maroon)}
.feat h3{font-size:9.5px;font-weight:600;color:var(--maroon);margin-top:16px;letter-spacing:.2px}
.feat p{font-size:6.5px;color:var(--muted);line-height:9.5px;margin:10px auto 0;width:140px}
.feat .more{font-size:6.5px;color:var(--maroon);margin-top:12px}
/* newsletter */
.news{left:0;top:622px;width:680px;height:113px;background:var(--maroon);color:#fff}
.news h2{position:absolute;left:26px;top:30px;font-family:'Raleway',sans-serif;font-weight:500;font-size:20px}
.news p{position:absolute;left:26px;top:58px;width:190px;font-size:6.5px;line-height:9px}
.email{left:224px;top:34px;width:321px;height:42px;border:1px solid rgba(255,255,255,.35);font-size:8px;padding-left:14px;line-height:42px;color:#eee}
.subscribe{left:545px;top:34px;width:104px;height:42px;background:var(--charcoal);font-family:'Raleway',sans-serif;font-weight:700;font-size:14px;text-align:center;line-height:42px;letter-spacing:.5px;border:1px solid rgba(255,255,255,.3)}
/* rooms */
.room{top:763px;width:194px}
.room .photo{height:113px}
.room h4{font-size:7px;font-weight:700;color:var(--maroon-deep);margin-top:15px}
.room p{font-size:6.5px;line-height:9.5px;color:var(--muted);margin-top:5px}
.room .btn{display:inline-block;margin-top:6px;font-size:6.5px;padding:0 8px;line-height:17px;border:1px solid var(--maroon);color:var(--maroon)}
.room .btn.fill{background:var(--maroon);color:#fff}
/* footer */
.footer{left:0;top:966px;width:680px;height:162px;background:var(--footer-bg)}
.col h5{font-size:9.5px;font-weight:400;color:var(--maroon);margin-bottom:10px}
.col p{font-size:6.5px;line-height:10.6px;color:#444;text-align:justify}
.col ul{list-style:none}
.col li{font-size:6.5px;color:#444;line-height:16px;padding-left:9px;position:relative}
.col li:before{content:"";position:absolute;left:0;top:7px;width:2px;height:2px;background:#777;border-radius:50%}
.divider{top:16px;width:1px;height:130px;background:rgba(255,255,255,.5)}
.readmore{display:inline-block;margin-top:9px;background:var(--maroon);color:#fff;font-size:6.5px;padding:0 11px;line-height:16px}
.bottom{left:0;top:1128px;width:680px;height:72px;background:var(--maroon);color:#fff}
.links{left:0;width:680px;top:26px;text-align:center;font-size:6.5px}
.copy{left:0;width:680px;top:43px;text-align:center;font-size:5.5px}
.social{right:26px;top:30px;display:flex;gap:14px}
.social span{width:8px;height:8px;border-radius:50%;background:#d9c6c8}
</style>
</head>
<body>
<header>
  <div class="abs topbar">
    <div class="abs brand">Lorven executive bed &amp; breakfast</div>
    <div class="abs call">
      <div class="ring"><svg width="11" height="11" viewBox="0 0 24 24"><path fill="#fff" d="M6.6 10.8a15 15 0 006.6 6.6l2.2-2.2c.3-.3.7-.4 1-.2 1.1.4 2.3.6 3.6.6.6 0 1 .4 1 1V20c0 .6-.4 1-1 1A17 17 0 013 4c0-.6.4-1 1-1h3.5c.6 0 1 .4 1 1 0 1.3.2 2.5.6 3.6.1.3 0 .7-.2 1z"/></svg></div>
      <div><small>CALL US</small><b>123-456-7890</b></div>
    </div>
  </div>
  <nav class="abs nav">
    <ul>
      <li class="active">HOME</li><li>B&amp;B ACCOMMODATION</li><li>GALLERY</li><li>WHAT'S NEARBY</li><li>GUEST BOOK</li><li>USEFUL LINKS</li><li>CONTACT US</li>
    </ul>
  </nav>
</header>

<section>
  <div class="abs hero" role="img" aria-label="Photo of the apartment living and dining room"></div>
  <form class="abs search">
    <div class="abs tab" style="left:28px"><svg width="16" height="12" viewBox="0 0 16 12"><path fill="#eee" d="M3 1h10l2 4v6h-2v-1H3v1H1V5zM4 2.5L3 5h10l-1-2.5zM3.5 6.5a1 1 0 100 2 1 1 0 000-2zm9 0a1 1 0 100 2 1 1 0 000-2z"/></svg>Car Rental</div>
    <div class="abs tab" style="left:111px"><svg width="16" height="12" viewBox="0 0 16 12"><path fill="#eee" d="M3 1h10l2 4v6h-2v-1H3v1H1V5zM4 2.5L3 5h10l-1-2.5zM3.5 6.5a1 1 0 100 2 1 1 0 000-2zm9 0a1 1 0 100 2 1 1 0 000-2z"/></svg>Car Rental</div>
    <div class="abs tab" style="left:192px"><svg width="16" height="12" viewBox="0 0 16 12"><path fill="#eee" d="M3 1h10l2 4v6h-2v-1H3v1H1V5zM4 2.5L3 5h10l-1-2.5zM3.5 6.5a1 1 0 100 2 1 1 0 000-2zm9 0a1 1 0 100 2 1 1 0 000-2z"/></svg>Car Rental</div>
    <div class="abs lbl" style="left:28px;top:82px">Going to</div>
    <div class="abs field" style="left:28px;top:95px;width:357px">
      <svg width="6" height="8" viewBox="0 0 12 16"><path fill="#ddd" d="M6 0a6 6 0 00-6 6c0 4.5 6 10 6 10s6-5.5 6-10a6 6 0 00-6-6zm0 8.5A2.5 2.5 0 116 3.5a2.5 2.5 0 010 5z"/></svg>Address</div>
    <div class="abs lbl" style="left:28px;top:124px">Check in</div>
    <div class="abs lbl" style="left:154px;top:124px">Check out</div>
    <div class="abs lbl" style="left:277px;top:124px">Room</div>
    <div class="abs field dim" style="left:28px;top:135px;width:108px"><svg width="8" height="8" viewBox="0 0 10 10"><path fill="#bbb" d="M1 2h8v7H1zM2 4v4h6V4zM2.5 1h1v2h-1zm4 0h1v2h-1z"/></svg>dd/mm/yyyy</div>
    <div class="abs field dim" style="left:154px;top:135px;width:108px"><svg width="8" height="8" viewBox="0 0 10 10"><path fill="#bbb" d="M1 2h8v7H1zM2 4v4h6V4zM2.5 1h1v2h-1zm4 0h1v2h-1z"/></svg>dd/mm/yyyy</div>
    <div class="abs field dim" style="left:277px;top:135px;width:108px"><svg width="8" height="8" viewBox="0 0 10 10"><circle cx="5" cy="3" r="2.2" fill="#bbb"/><path fill="#bbb" d="M1 10c0-3 2-4.5 4-4.5S9 7 9 10z"/></svg>Number</div>
    <div class="abs lbl" style="left:28px;top:162px">Traveling For</div>
    <div class="abs field" style="left:28px;top:175px;width:357px">
      <svg width="6" height="8" viewBox="0 0 12 16"><path fill="#ddd" d="M6 0a6 6 0 00-6 6c0 4.5 6 10 6 10s6-5.5 6-10a6 6 0 00-6-6zm0 8.5A2.5 2.5 0 116 3.5a2.5 2.5 0 010 5z"/></svg>Work &nbsp;- &nbsp;Leisure
      <span style="margin-left:auto;padding:0 9px;font-size:6.5px;background:rgba(110,106,102,.8);line-height:19px">Not sure?</span></div>
    <div class="abs btn-search">SEARCH</div>
  </form>
</section>

<section>
  <div class="abs feat" style="left:34px;top:459px">
    <div class="circle light"><svg width="22" height="22" viewBox="0 0 22 22"><path fill="none" stroke="#5a0712" stroke-width="3" d="M3 20V3h8v12M11 2v0M8 8v12M19 2v17h-8"/></svg></div>
    <h3>LATEST MODEL HOTELS</h3>
    <p>Lorem ipsum dolor sit amet, consectetur adipiscing elit, sed do eiusmod</p>
    <div class="more">READ MORE &#9656;</div>
  </div>
  <div class="abs feat" style="left:242px;top:459px">
    <div class="circle"><svg width="30" height="30" viewBox="0 0 30 30"><circle cx="15" cy="10" r="6.5" fill="#fff"/><path fill="#fff" d="M3 28c0-7 5-11 12-11s12 4 12 11z"/></svg></div>
    <h3>BEST PRICE GUARANTEED</h3>
    <p>Lorem ipsum dolor sit amet, consectetur adipiscing elit, sed do eiusmod</p>
    <div class="more">READ MORE &#9656;</div>
  </div>
  <div class="abs feat" style="left:420px;top:459px">
    <div class="circle"><svg width="24" height="30" viewBox="0 0 24 30"><rect x="2" y="1" width="20" height="28" fill="none" stroke="#fff" stroke-width="2"/><g fill="#fff"><rect x="6" y="5" width="3" height="3"/><rect x="11" y="5" width="3" height="3"/><rect x="16" y="5" width="3" height="3"/><rect x="6" y="10" width="3" height="3"/><rect x="11" y="10" width="3" height="3"/><rect x="16" y="10" width="3" height="3"/><rect x="6" y="15" width="3" height="3"/><rect x="11" y="15" width="3" height="3"/><rect x="16" y="15" width="3" height="3"/><rect x="9" y="22" width="6" height="7"/></g></svg></div>
    <h3>FREE CANCELLATION</h3>
    <p>Lorem ipsum dolor sit amet, consectetur adipiscing elit, sed do eiusmod</p>
    <div class="more">READ MORE &#9656;</div>
  </div>
</section>

<section class="abs news">
  <h2>Newsletter Sign Up</h2>
  <p>Lorem ipsum dolor sit amet conse ctetur adipisicing elit, sed do eiusmod tempor incididunt ut labore</p>
  <div class="abs email">Enter Your E-Mail Id</div>
  <div class="abs subscribe">SUBSCRIBE</div>
</section>

<section>
  <article class="abs room" style="left:26px">
    <div class="photo" role="img" aria-label="Photo of the open-plan lounge with television" style="background:linear-gradient(135deg,#c9b48a,#8a6d48)"></div>
    <h4>LOREM IPSUM DOLOR SIT AMET</h4>
    <p>Lorem ipsum dolor sit amet, consectetur adipiscing elit, sed do eiusmod tempor incididunt</p>
    <span class="btn fill">READ MORE</span>
  </article>
  <article class="abs room" style="left:243px">
    <div class="photo" role="img" aria-label="Photo of the courtyard garden beside the entrance" style="background:linear-gradient(135deg,#d8cfb8,#6f7a4a 60%,#4d5a30)"></div>
    <h4>LOREM IPSUM DOLOR SIT AMET</h4>
    <p>Lorem ipsum dolor sit amet, consectetur adipiscing elit, sed do eiusmod tempor incididunt</p>
    <span class="btn">READ MORE</span>
  </article>
  <article class="abs room" style="left:460px">
    <div class="photo" role="img" aria-label="Photo of the bedroom with red bedspread" style="background:linear-gradient(180deg,#b89a6e 0%,#c8a878 45%,#c0101a 60%,#a00d16)"></div>
    <h4>LOREM IPSUM DOLOR SIT AMET</h4>
    <p>Lorem ipsum dolor sit amet, consectetur adipiscing elit, sed do eiusmod tempor incididunt</p>
    <span class="btn">READ MORE</span>
  </article>
</section>

<footer>
  <div class="abs footer" role="img" aria-label="Faint backdrop of world landmarks">
    <div class="abs col" style="left:29px;top:30px;width:174px">
      <h5>About Us</h5>
      <p>Lorem ipsum dolor sit amet, consectetur adipiscing elit, sed do eiusmod tempor incididunt ut labore et dolore magna aliqua. Ut enim ad minim veniam, quis nostrud exercitation ullamco laboris tempor incididunt ut labore et dolore magna aliqua. Ut enim ad minim veniam, quis nostrud exercitation ullamco laboris</p>
      <span class="readmore">Read More</span>
    </div>
    <div class="abs divider" style="left:232px"></div>
    <div class="abs col" style="left:248px;top:30px">
      <h5>Cover</h5>
      <ul><li>Pre-existing Medical Conditions</li><li>Product Disclosure Statement (PDS)</li><li>Seniors Travel Insurance</li><li>Family Travel Insurance</li><li>Working Holiday</li><li>Multi-Trip Cover</li></ul>
    </div>
    <div class="abs divider" style="left:395px"></div>
    <div class="abs col" style="left:414px;top:30px">
      <h5>Support</h5>
      <ul><li>Make a change to Your</li><li>Ask a Question</li><li>Frequently Asked Question</li><li>Make a Claim</li><li>Contacts</li></ul>
    </div>
    <div class="abs divider" style="left:550px"></div>
    <div class="abs col" style="left:570px;top:30px">
      <h5>About</h5>
      <ul><li>Contacts</li><li>Blog</li><li>Privacy Policy</li><li>Duty of Disclosure</li><li>sponsorships</li></ul>
    </div>
  </div>
  <div class="abs bottom">
    <div class="abs links">Home &nbsp;/ &nbsp;About Us &nbsp;/ &nbsp;Our Services &nbsp;/ &nbsp;Testimonials &nbsp;/ &nbsp;Gallery &nbsp;/ &nbsp;Contact</div>
    <div class="abs copy">&copy; All Rights Reserved. Copyrights @Company name</div>
    <div class="abs social" aria-label="Social links"><span></span><span></span><span></span><span></span><span></span></div>
  </div>
</footer>
</body>
</html>
```